Looking for business card/letterhead/email signature

Take existing logo and create full design suite of collateral

Contact Information for Business Card

Use mock details that can be edited by us

Font styles to use
Sans Serif

```html
<!DOCTYPE html>
<html lang="en">
<head>
<meta charset="utf-8">
<title>Harlow Digital – Business Card</title>
<link href="https://fonts.googleapis.com/css2?family=Lato:wght@400;700&family=Montserrat:wght@600;700&display=swap" rel="stylesheet">
<style>
  :root {
    --stage: #1c1d20;
    --brand-blue: #0a5aaa;
    --brand-blue-deep: #064789;
    --brand-navy: #0b3f86;
    --accent-pink: #e0175f;
    --paper: #ffffff;
    --paper-shade: #eef1f5;
    --ink-light: #ffffff;
  }
  * { margin: 0; padding: 0; box-sizing: border-box; }
  html, body { width: 1200px; height: 896px; overflow: hidden; }
  body {
    background: var(--stage);
    font-family: "Lato", sans-serif;
    position: relative;
  }
  .card {
    position: absolute;
    top: 158px;
    width: 340px;
    height: 580px;
    border-radius: 22px;
    overflow: hidden;
    box-shadow: 0 18px 40px rgba(0,0,0,.5);
  }
  .card--front {
    left: 190px;
    background: linear-gradient(160deg, #1769bd 0%, var(--brand-blue) 45%, var(--brand-blue-deep) 100%);
    display: flex;
    align-items: center;
    justify-content: center;
  }
  .card--back { left: 670px; background: var(--paper); }

  .wordmark {
    display: flex;
    align-items: center;
    gap: 10px;
    font-family: "Montserrat", sans-serif;
    font-weight: 700;
    font-size: 34px;
    letter-spacing: -0.5px;
    line-height: 1;
  }
  .wordmark__dot {
    width: 14px; height: 14px; border-radius: 50%;
    background: currentColor;
  }
  .card--front .wordmark { color: var(--ink-light); }
  .card--back .wordmark { color: var(--brand-navy); }

  .back__top {
    height: 262px;
    background: linear-gradient(180deg, var(--paper) 60%, var(--paper-shade) 100%);
    display: flex;
    align-items: center;
    justify-content: center;
  }
  .back__divider { height: 4px; background: var(--accent-pink); }
  .back__bottom {
    height: 314px;
    background: linear-gradient(170deg, #0d5fb1 0%, var(--brand-blue-deep) 100%);
    color: var(--ink-light);
    padding: 30px 30px 0 32px;
  }
  .person__name {
    font-family: "Montserrat", sans-serif;
    font-weight: 600;
    font-size: 21px;
  }
  .person__title { font-size: 15px; margin-top: 2px; }
  .person__rule { width: 32px; height: 3px; background: var(--ink-light); margin: 12px 0 14px; }
  .company__name { font-weight: 700; font-size: 17px; }
  .company__address { font-size: 14px; line-height: 1.3; margin-top: 2px; }
  .contact-list { list-style: none; margin-top: 16px; font-size: 14.5px; }
  .contact-list li { display: flex; align-items: center; gap: 12px; height: 22px; }
  .contact-list svg { width: 14px; height: 14px; flex: none; }
</style>
</head>
<body>
  <section class="card card--front" aria-label="Card front">
    <div class="wordmark"><span class="wordmark__dot"></span>harlow digital</div>
  </section>

  <section class="card card--back" aria-label="Card back">
    <div class="back__top">
      <div class="wordmark"><span class="wordmark__dot"></span>harlow digital</div>
    </div>
    <div class="back__divider"></div>
    <div class="back__bottom">
      <p class="person__name">Marcus Trent</p>
      <p class="person__title">Chief Executive Officer</p>
      <div class="person__rule"></div>
      <p class="company__name">harlow digital</p>
      <p class="company__address">4820 Coral Ridge Ave.<br>Bayview Heights<br>FL 33000</p>
      <ul class="contact-list">
        <li>
          <svg viewBox="0 0 16 16" fill="none" stroke="#fff" stroke-width="1.6"><path d="M3 2h3l1.5 3.5-2 1.2a8 8 0 0 0 3.8 3.8l1.2-2L14 10v3a1 1 0 0 1-1 1A11 11 0 0 1 2 3a1 1 0 0 1 1-1z"/></svg>
          (555) 014-2290
        </li>
        <li>
          <svg viewBox="0 0 16 16" fill="none" stroke="#fff" stroke-width="1.6"><rect x="2" y="6" width="12" height="7" rx="1"/><path d="M4 6V2h8v4M5 10h6"/></svg>
          (555) 014-7781
        </li>
        <li>
          <svg viewBox="0 0 16 16" fill="none" stroke="#fff" stroke-width="1.6"><rect x="1.5" y="3.5" width="13" height="9" rx="1"/><path d="M2 4l6 5 6-5"/></svg>
          hello@HarlowDigital.com
        </li>
        <li>
          <svg viewBox="0 0 16 16" fill="none" stroke="#fff" stroke-width="1.4"><circle cx="8" cy="8" r="6.5"/><ellipse cx="8" cy="8" rx="3" ry="6.5"/><path d="M1.5 8h13"/></svg>
          www.HarlowDigital.com
        </li>
      </ul>
    </div>
  </section>
</body>
</html>
```